Bright Path Attorneys Billboard Design for Personal Injury Law Firm

Need a billboard design that we can use for different versions. 1400px X 400px jpeg or png
I have attached the logo and the attorney for the billboard. Attorney Marla Benning
Here is a link to our current website brightpathlegalgroup.example

HEADLINE: HIT BY A TRUCK?
SUBHEAD: NO FEE. BIG FIGHT.
877-GRANTLY

HEADLINE: ACCIDENT?
SUBHEAD: NO FEE, UNLESS WE WIN!
877-GRANTLY

HEADLINE: BIG TRUCK. BIG CASE.
SUBHEAD: YOU PAY $0 UPFRONT
877-GRANTLY

Target Market(s)

People in Car Accident

Industry/Entity Type

Personal Injury Attorneys

```html
<!DOCTYPE html>
<html lang="en">
<head>
<meta charset="utf-8">
<title>Bright Path Attorneys Billboard</title>
<link rel="stylesheet" href="https://fonts.googleapis.com/css2?family=Poppins:wght@600;700;800&display=swap">
<style>
  :root {
    --navy: #08101a;
    --navy-deep: #050a12;
    --green: #5fd94a;
    --green-dark: #3a9a30;
    --cream: #fbf6e8;
    --ink: #0a0c0a;
  }
  html, body {
    margin: 0;
    padding: 0;
    width: 1200px;
    height: 343px;
    overflow: hidden;
    background: var(--navy-deep);
  }
  .billboard {
    position: relative;
    width: 1200px;
    height: 343px;
    overflow: hidden;
    background: var(--navy);
    font-family: "Poppins", sans-serif;
  }
  .edge-glow {
    position: absolute;
    left: 0; top: 0;
    width: 70px; height: 100%;
    background: linear-gradient(90deg, rgba(95,217,74,0.5), rgba(95,217,74,0));
  }
  .scene-photo {
    position: absolute;
    right: 0; top: 0;
    width: 560px; height: 100%;
    background:
      linear-gradient(90deg, var(--navy) 0%, rgba(8,16,26,0.6) 22%, rgba(8,16,26,0) 45%),
      radial-gradient(circle at 72% 30%, #c98a4a 0%, rgba(201,138,74,0) 30%),
      linear-gradient(180deg, #59606a 0%, #2d343c 45%, #474c52 72%, #2a2e33 100%);
  }
  .brand {
    position: absolute;
    left: 44px; top: 30px;
    height: 36px;
    display: flex;
    align-items: center;
    gap: 12px;
    color: var(--cream);
    font-weight: 700;
    font-size: 19px;
    letter-spacing: 0.5px;
    text-transform: uppercase;
  }
  .brand-mark {
    width: 34px; height: 34px;
    background: var(--green);
  }
  .headline {
    position: absolute;
    left: 40px; top: 80px;
    margin: 0;
    color: var(--green);
    font-weight: 800;
    font-size: 96px;
    line-height: 1;
    letter-spacing: 0.5px;
    white-space: nowrap;
  }
  .subhead {
    position: absolute;
    left: 42px; top: 174px;
    margin: 0;
    color: var(--cream);
    font-weight: 700;
    font-size: 48px;
    line-height: 1;
    letter-spacing: 4px;
    white-space: nowrap;
  }
  .phone-band {
    position: absolute;
    left: 0; top: 255px;
    width: 800px; height: 64px;
    background: linear-gradient(90deg, var(--green) 0%, var(--green) 45%, var(--green-dark) 75%, rgba(58,154,48,0) 100%);
    display: flex;
    align-items: center;
  }
  .phone-number {
    margin-left: 40px;
    color: var(--ink);
    font-weight: 700;
    font-size: 48px;
    line-height: 1;
    letter-spacing: 0.5px;
  }
</style>
</head>
<body>
  <div class="billboard">
    <div class="scene-photo" role="img" aria-label="Photo of a silver car with a crushed front end parked at a roadside curb at sunset"></div>
    <div class="edge-glow"></div>
    <div class="brand"><span class="brand-mark"></span>Bright Path Attorneys</div>
    <h1 class="headline">ACCIDENT?</h1>
    <p class="subhead">NO FEE, UNLESS WE WIN!</p>
    <div class="phone-band"><span class="phone-number">877-GRANTLY</span></div>
  </div>
</body>
</html>
```